Lumaridge Hauling

WHY: So we are looking for a clean blue/modern/ mobile friendly website to be able compete with our rival, which is bellhops.comWHO: Our company is based out Atlanta,GA. The Company named is called "LumaRidge Hauling" and we are Professional staffing Agency that trained our employees for Household Industry related tasks such as Moving Furniture, Packers Household Boxes , Vondra Furniture Installers, Mounting TV and etc.WHAT: Our Main Function is we need to be able to pre-qualified lead/schedule them based on availability /Book our client online on Quenpay in order to help our client solve and their problem faster than the traditional 20 min phone call. We need an :Pre-Survey Form /Basic Contact Form Example Below...Desired Button Placement: Should be In the Center or Right Corner. * Q1. What would you like help with? (multi-Choice A to D?* Q2. What are you packing or unpacking* Q3. How many boxes would you like packed or unpacked?* Q4.In Additional to packing or unpacking, do you need any other service>* Q5. Would you like to add photos of the primary item you need packed on..* Q6. When would you like the packing specialist?* Q7. WHat time work best for your schedule?* Q8.Anything else the packing specialist should know? * Q8. Zip Code * Q9. Name* Q10. Email (Privacy Disclaimer)* Q12. Number * Q13. Customer Credit Card InfoWHEN: we looking to be done submit all of our revision request and the project done before New Year, Jan.1

Target Market(s)

Womans: Between 25yr to +55 Womans, Affluence,

Industry/Entity Type

Moving

Number of Pages Required

2 page

Font styles to use
Sans Serif

Colors

Designer to choose colors to be used in the design.

Requirements
Must have
• Service Option Category
• Packers/Installer/ Rental Trucks Assistant
• How it Work Session
• 1.Pick a Service
• 2.Book A Time
• 3.Secured A Payment
Nice to have
• Our Main Function is we need to be able to pre-qualified lead/schedule them based on availability /Book our client online on Quenpay in order to help our client solve and their problem faster than the traditional 20 min phone call.
• We need an :Pre-Survey Form /Basic Contact Form Example Below...
• Desired Button Placement: Should be In the Center or Right Corner.
• * Q1. What would you like help with? (multi-Choice A to D?
• * Q2. What are you packing or unpacking
• * Q3. How many boxes would you like packed or unpacked?
• * Q4.In Additional to packing or unpacking, do you need any other service>
• * Q5. Would you like to add photos of the primary item you need packed on..
• * Q6. When would you like the packing specialist?
• * Q7. WHat time work best for your schedule?
• * Q8.Anything else the packing specialist should know?
• * Q8. Zip Code
• * Q9. Name
• * Q10. Email (Privacy Disclaimer)
• * Q12. Number
• * Q13. Customer Credit Card Info
Should not have
• we are not interesting for an Basic Template Design /generic Truck photo stock/ traditional moving company website).

```html
<!DOCTYPE html>
<html lang="en">
<head>
<meta charset="utf-8">
<title>LumaRidge Hauling — Book a local athlete</title>
<link href="https://fonts.googleapis.com/css2?family=Varela+Round&family=Open+Sans:wght@400;600;700&family=Lato:wght@300;400&family=Crimson+Text&display=swap" rel="stylesheet">
<style>
  :root {
    --stage: #0d1630;
    --hero-dark: #2e3033;
    --hero-light: #6b6d70;
    --white: #ffffff;
    --ink: #333333;
    --ink-soft: #444444;
    --section-soft: #f7f7f7;
    --card: #ffffff;
    --accent: #2f6fe8;
    --works-bg: #4b4b4c;
    --works-field: #5f5f60;
    --works-box: #6e6e6e;
  }
  * { margin: 0; padding: 0; box-sizing: border-box; }
  html, body { width: 1200px; height: 1200px; overflow: hidden; background: var(--stage); }
  .page {
    position: absolute; left: 333.6px; top: 0;
    width: 666px; height: 1500px;
    transform: scale(0.8); transform-origin: 0 0;
    font-family: "Open Sans", sans-serif; color: var(--ink);
    overflow: hidden;
  }
  .abs { position: absolute; }
  .center { left: 0; width: 666px; text-align: center; }

  /* Hero */
  .hero { left: 0; top: 0; width: 666px; height: 341px;
    background: radial-gradient(ellipse at 55% 45%, var(--hero-light) 0%, #4b4d50 45%, var(--hero-dark) 100%); }
  .brand { left: 66px; top: 20px; font-family: "Varela Round", sans-serif; font-size: 15px; color: var(--white); }
  .nav a { position: absolute; top: 27px; font-size: 7px; letter-spacing: 1px; color: var(--white); text-decoration: none; font-weight: 600; }
  .nav .active { border-bottom: 1px solid var(--white); padding-bottom: 4px; }
  .hero-title { top: 138px; font-family: "Varela Round", sans-serif; font-size: 28px; line-height: 31px; color: var(--white); letter-spacing: 0.5px; }

  /* Services */
  .services { left: 0; top: 341px; width: 666px; height: 401px; background: var(--section-soft); }
  .section-title { font-family: "Varela Round", sans-serif; font-size: 28px; color: var(--ink); }
  .service-card { top: 459px; width: 137px; height: 146px; background: var(--card); padding: 12px 14px; color: var(--ink); }
  .service-card h3 { font-size: 8.5px; font-weight: 600; text-align: center; margin-bottom: 14px; color: var(--ink); }
  .service-card ul { color: var(--ink-soft); }
  .service-card li { list-style: none; font-size: 8px; font-weight: 600; line-height: 10.5px; color: var(--ink-soft); margin-bottom: 11px; }
  .btn { background: var(--accent); color: var(--white); border-radius: 13px; text-align: center; font-size: 6px; letter-spacing: 0.6px; line-height: 25px; height: 25px; }

  /* Testimonials */
  .why { left: 0; top: 742px; width: 666px; height: 408px; background: var(--white); }
  .why-sub { font-family: "Varela Round", sans-serif; font-size: 15px; line-height: 15px; color: var(--ink); }
  .testimonial { left: 54px; top: 877px; width: 174px; height: 222px; background: var(--card); box-shadow: 0 1px 6px rgba(0,0,0,0.15); }
  .avatar { left: 46px; top: 17px; width: 82px; height: 82px; border-radius: 50%; background: radial-gradient(circle at 50% 45%, #e6c7b4 0%, #b98d74 55%, #e9d6d8 100%); }
  .quote { left: 14px; top: 111px; width: 146px; text-align: center; font-family: "Crimson Text", serif; font-size: 8.5px; line-height: 10px; color: #555; }
  .author { left: 0; top: 175px; width: 174px; text-align: center; font-size: 6.5px; font-weight: 600; letter-spacing: 0.6px; color: var(--ink); }
  .video { left: 296px; top: 900px; width: 282px; height: 171px; background: #000; }
  .video-bar { left: 0; bottom: 0; width: 282px; height: 14px; background: #1b1b1b; }
  .video-time { left: 44px; top: 4px; font-size: 5px; color: #bbb; }

  /* How it works */
  .works { left: 0; top: 1150px; width: 666px; height: 350px; background: var(--works-bg); color: var(--white); }
  .works-title { top: 40px; font-family: "Lato", sans-serif; font-weight: 300; font-size: 27px; }
  .q { font-size: 11px; font-weight: 600; letter-spacing: 0.7px; }
  .opt { font-size: 9.5px; font-weight: 600; letter-spacing: 0.4px; padding-left: 16px; }
  .opt::before { content: ""; position: absolute; left: 0; top: 4px; width: 6px; height: 6px; border: 1px solid var(--works-box); }
  .opt.radio::before { border-radius: 50%; }
  .field { background: var(--works-field); font-size: 6.5px; text-align: center; line-height: 24px; height: 24px; width: 70px; color: var(--white); }
  .note { font-size: 6.5px; font-weight: 700; line-height: 7.5px; letter-spacing: 0.3px; }
</style>
</head>
<body>
<main class="page">

  <header class="abs hero" role="img" aria-label="Black and white photo of an athlete lifting a barbell in a gym"></header>
  <div class="abs brand">LumaRidge Hauling</div>
  <nav class="nav">
    <a style="left:397px">HOME</a>
    <a class="active" style="left:444px">ABOUT US</a>
    <a style="left:505px">TESTIMONIAL</a>
    <a style="left:571px">CONTACT</a>
  </nav>
  <h1 class="abs center hero-title">Book a local<br>lumaridge athlete</h1>

  <section class="abs services"></section>
  <h2 class="abs center section-title" style="top:397px">What we do?</h2>

  <article class="abs service-card" style="left:47px">
    <h3>Packing / Boxes</h3>
    <ul><li>· Lorem ipsum dolor sit amet, consectetur</li><li>· Adipisicing elit, sed do</li><li>· Eiusmod tempor incididunt ut labore et</li><li>· Dolore magna aliqua.</li></ul>
  </article>
  <article class="abs service-card" style="left:189px">
    <h3>Transporting</h3>
    <ul><li>· Lorem ipsum dolor sit amet, consectetur</li><li>· Adipisicing elit, sed do</li><li>· Eiusmod tempor incididunt ut labore et</li><li>· Dolore magna aliqua.</li></ul>
  </article>
  <article class="abs service-card" style="left:331px">
    <h3>Packing PODs</h3>
    <ul><li>· Lorem ipsum dolor sit amet, consectetur</li><li>· Adipisicing elit, sed do</li><li>· Eiusmod tempor incididunt ut labore et</li><li>· Dolore magna aliqua.</li></ul>
  </article>
  <article class="abs service-card" style="left:473px">
    <h3>Installation</h3>
    <ul><li>· Lorem ipsum dolor sit amet, consectetur</li><li>· Adipisicing elit, sed do</li><li>· Eiusmod tempor incididunt ut labore et</li><li>· Dolore magna aliqua.</li></ul>
  </article>
  <div class="abs btn" style="left:288px;top:657px;width:90px">BOOK NOW</div>

  <section class="abs why"></section>
  <h2 class="abs center section-title" style="top:773px">Why us?</h2>
  <p class="abs center why-sub" style="top:809px">This is what people<br>is saying...</p>

  <svg class="abs" style="left:25px;top:981px" width="12" height="16" viewBox="0 0 12 16"><path d="M9 1 L3 8 L9 15" fill="none" stroke="#999" stroke-width="1.2"/></svg>
  <svg class="abs" style="left:246px;top:981px" width="12" height="16" viewBox="0 0 12 16"><path d="M3 1 L9 8 L3 15" fill="none" stroke="#999" stroke-width="1.2"/></svg>

  <figure class="abs testimonial">
    <div class="abs avatar" role="img" aria-label="Portrait photo of the reviewer"></div>
    <blockquote class="abs quote">Aliquip ex ea commodo consequat. Duis aute irure dolor in reprehenderit in voluptate velit esse cillum dolore eu fugiat nulla pariatur.</blockquote>
    <figcaption class="abs author">CORINNE ALDWAY</figcaption>
  </figure>

  <div class="abs video" role="img" aria-label="Customer testimonial video">
    <svg class="abs" style="left:0;top:153px" width="282" height="4"><rect width="282" height="3" fill="#444"/><circle cx="3" cy="1.5" r="2.5" fill="#ddd"/></svg>
    <div class="abs video-bar">
      <svg class="abs" style="left:10px;top:4px" width="30" height="7"><path d="M0 0 L5 3.5 L0 7Z" fill="#999"/><path d="M18 2 H20 L23 0 V7 L20 5 H18Z" fill="#999"/></svg>
      <span class="abs video-time">0:00 / 3:43</span>
      <svg class="abs" style="left:232px;top:4px" width="44" height="7"><circle cx="3" cy="3.5" r="2.5" fill="#999"/><circle cx="14" cy="3.5" r="2.5" fill="none" stroke="#999"/><rect x="22" y="1" width="8" height="5" fill="none" stroke="#999"/><rect x="35" y="0.5" width="7" height="6" fill="none" stroke="#999" stroke-dasharray="2 2"/></svg>
    </div>
  </div>

  <section class="abs works">
    <h2 class="abs center works-title">How it works</h2>

    <p class="abs q" style="left:63px;top:82px">What do you need?</p>
    <span class="abs opt" style="left:63px;top:105px">Packing</span>
    <span class="abs opt" style="left:181px;top:105px">Packing PODs</span>
    <span class="abs opt" style="left:63px;top:127px">Transporting</span>
    <span class="abs opt" style="left:181px;top:127px">Installation</span>

    <p class="abs q" style="left:386px;top:82px">How many boxes we'll be needing?</p>
    <span class="abs opt radio" style="left:386px;top:105px">More than 2</span>
    <span class="abs opt radio" style="left:503px;top:105px">More than 10</span>

    <p class="abs q" style="left:63px;top:161px">What are you packing/unpacking?</p>
    <span class="abs opt" style="left:63px;top:184px">Couches</span>
    <span class="abs opt" style="left:181px;top:184px">Electronics</span>
    <span class="abs opt" style="left:63px;top:206px">Instruments</span>
    <span class="abs opt" style="left:181px;top:206px">Machines</span>

    <p class="abs q" style="left:386px;top:161px">Let's set a date, and a time</p>
    <div class="abs field" style="left:388px;top:184px">MM/DD/YYYY</div>
    <div class="abs field" style="left:490px;top:184px">15:30</div>

    <p class="abs center note" style="top:266px">You'll have to give us a few more details<br>in the next stage</p>
    <div class="abs btn" style="left:289px;top:295px;width:88px">Book now</div>
  </section>

</main>
</body>
</html>
```